GPS Tracker Business Card Design

We need a business card for a GPS Vehicle tracking company. We sell the hardware for the vehicle and the software platform to monitor your vehicle/s. Including high asset non-powered vehicles like a trailer using our solar powered unit.
We like using dark blue to different shades of blue along with gold. We have phone apps for Android and Apple devices.

We have a platform for families wanting to track their teenage driver and children; Plus a Fleet vehicle tracking platform.

Features: unlimited number of vehicles and/or assets including snow mobiles forklifts generators trailers airport equipment

Reports for driving behavior reports and alerts dashboard fleet maintenace timeline view and replay geofence real time alerts logbook scheduling route optimization accounting integration fleet grouping closest vehicle locator On Board Diagnostics.

Benefits: Increased productivity improved fuel efficiency organizing your business improve time management simplify back end processes, reduce fleet fuel efficiency and expenses increase fleet security etc..

Please view website: Velmora.com

Industry/Entity Type

Business

Contact Information for Business Card

Harold B Pennick

```html
<!DOCTYPE html>
<html lang="en">
<head>
<meta charset="utf-8">
<title>Velmora Business Card</title>
<link rel="stylesheet" href="https://fonts.googleapis.com/css2?family=Montserrat:wght@300;400;600&family=PT+Sans+Narrow&display=swap">
<style>
  :root {
    --stage: #4a4a4a;
    --card: #ffffff;
    --brand-blue: #0b4f9e;
    --ink: #1c1c1c;
    --tagline: #6b6b6b;
    --icon-blue: #3a8fc8;
    --badge-green: #5aa63a;
    --badge-grey: #a9a9a9;
  }
  * { margin: 0; padding: 0; box-sizing: border-box; }
  html, body {
    width: 1105px; height: 1200px; overflow: hidden;
    background: var(--stage);
    font-family: "Montserrat", Arial, sans-serif;
  }
  .card {
    position: absolute; left: 196px; width: 720px; height: 410px;
    background: var(--card); overflow: hidden;
  }
  .card--front { top: 146px; }
  .card--back { top: 602px; }

  .wordmark {
    position: absolute; left: 0; right: 0; text-align: center;
    font-weight: 300; font-size: 84px; line-height: 1;
    color: var(--brand-blue); letter-spacing: -1px;
  }
  .tagline {
    position: absolute; left: 0; right: 0; text-align: center;
    font-weight: 400; font-size: 24px; color: var(--tagline);
  }
  .card--front .wordmark { top: 52px; }
  .card--front .tagline { top: 132px; }
  .card--back .wordmark { top: 164px; }
  .card--back .tagline { top: 246px; }

  .band { position: absolute; left: 0; top: 0; width: 720px; height: 410px; }

  .holder { position: absolute; left: 36px; top: 266px; color: #fff; }
  .holder__name { font-weight: 600; font-size: 26px; line-height: 34px; }
  .holder__title, .holder__address { font-weight: 400; font-size: 20px; line-height: 28px; }
  .holder__title { margin-bottom: 4px; }

  .contact {
    position: absolute; right: 24px; top: 272px; list-style: none;
    color: #fff; font-size: 20px; line-height: 28px; text-align: right;
  }
  .contact li { display: flex; justify-content: flex-end; align-items: center; gap: 14px; }
  .contact svg { width: 18px; height: 18px; fill: #fff; }

  .social { position: absolute; left: 41px; top: 33px; display: flex; gap: 6px; }
  .social span { width: 34px; height: 34px; border-radius: 6px; background: var(--icon-blue); }
  .stores { position: absolute; right: 20px; top: 17px; display: flex; gap: 8px; }
  .stores span { width: 34px; height: 34px; border-radius: 50%; }
  .stores .store--primary { background: var(--badge-green); }
  .stores .store--secondary { background: var(--badge-grey); }

  .benefits {
    position: absolute; left: 0; right: 0; top: 340px; text-align: center;
    font-family: "PT Sans Narrow", "Arial Narrow", sans-serif;
    font-size: 21px; color: var(--ink);
  }
  .benefits .dot { color: var(--brand-blue); padding: 0 4px; }
</style>
</head>
<body>
  <section class="card card--front">
    <div class="wordmark">Velmora</div>
    <div class="tagline">Every Road, Every Mile</div>
    <svg class="band" viewBox="0 0 720 410" aria-hidden="true">
      <path d="M0 238 Q360 190 720 242" fill="none" stroke="#111" stroke-width="3"/>
      <path d="M0 246 Q360 200 720 250 L720 410 L0 410 Z" fill="var(--brand-blue)"/>
    </svg>
    <div class="holder">
      <div class="holder__name">Harold B Pennick</div>
      <div class="holder__title">CEO/Founder</div>
      <div class="holder__address">214 Larkspur Court</div>
      <div class="holder__address">Fairbanks, Alaska 99701</div>
    </div>
    <ul class="contact">
      <li>555-014-2871
        <svg viewBox="0 0 24 24"><path d="M6.6 10.8a15 15 0 0 0 6.6 6.6l2.2-2.2c.3-.3.7-.4 1-.2 1.1.4 2.3.6 3.6.6.6 0 1 .4 1 1V20c0 .6-.4 1-1 1A17 17 0 0 1 3 4c0-.6.4-1 1-1h3.5c.6 0 1 .4 1 1 0 1.3.2 2.5.6 3.6.1.3 0 .7-.2 1z"/></svg></li>
      <li>555 017 6630
        <svg viewBox="0 0 24 24"><path d="M6 2h12v6H6zM3 9h18v9h-3v4H6v-4H3zm5 6v5h8v-5z"/></svg></li>
      <li>hello@velmora.com
        <svg viewBox="0 0 24 24"><path d="M2 5h20v14H2zm2 2v.5l8 5.5 8-5.5V7z"/></svg></li>
      <li>www.velmora.com
        <svg viewBox="0 0 24 24"><circle cx="12" cy="12" r="10"/><path d="M7 8c2 0 3 1 3 3s-2 2-2 4 1 3 0 4M15 5c-1 2 1 3 2 3s2 2 1 4" stroke="var(--brand-blue)" stroke-width="2" fill="none"/></svg></li>
    </ul>
  </section>

  <section class="card card--back">
    <div class="social" aria-label="Social channels">
      <span></span><span></span><span></span><span></span>
    </div>
    <div class="stores" aria-label="Mobile app stores">
      <span class="store--primary"></span><span class="store--secondary"></span>
    </div>
    <div class="wordmark">Velmora</div>
    <div class="tagline">Every Road, Every Mile</div>
    <p class="benefits">Exceptional hardware &amp; software <span class="dot">&#9679;</span> Excellent Customer Service <span class="dot">&#9679;</span> Low Price</p>
  </section>
</body>
</html>
```